"Here We Go" Dance Production Poster

This is a dance school annual theatre performance, at the Lanworth Guild Playhouse. The dates are from the 26th-28th July 2012, and the show is called "Here We Go."

Although not themed around Desmond Farrow specifically, we are using a few songs hence the title.

We need an eye catching poster with out focusing too much around DF. Maybe even using his theme/image subliminally but must look professional and vivid.

We are a dance school predominantly female based with a few males - age range 2-55
Updates

Hi guys - please check brief 

We are getting to many designs based too much around Desmond Farrow

This only has to be subliminal as the show isn't about him, it's mainly a generic dance show

Please try to bare this in mind

Thanks

Target Market(s)

Parents, family, friends of the performers/general public

Industry/Entity Type

School

Requirements
Must have
• The Hollis Brandt School Of Dance Present "Here We Go"
26th-28th July 2012 at the Lanworth Guild

Tickets available from the Theatre Box Office

www.hbschoolofdance-example.co.uk

Nice to have
• Subliminal Desmond Farrow feel - no pictures of him though
Should not have
• Cheap templates, poor images, flowery fonts

```html
<!DOCTYPE html>
<html lang="en">
<head>
<meta charset="utf-8">
<title>Here We Go – Annual Theatre Performance</title>
<link href="https://fonts.googleapis.com/css2?family=Arimo:wght@400;700&family=Cinzel:wght@400;600&display=swap" rel="stylesheet">
<style>
  :root {
    --page-bg: #2a2a2a;
    --band-dark: #06203f;
    --band-mid: #163f6e;
    --ink: #1c1c1c;
    --white: #ffffff;
    --sky: #d9f1f4;
    --aqua: #9fd9d8;
    --lime: #b4d633;
    --green: #7fae1c;
  }
  * { margin: 0; padding: 0; box-sizing: border-box; }
  html, body { width: 1200px; height: 901px; overflow: hidden; }
  body { background: var(--page-bg); position: relative; font-family: "Arimo", Arial, sans-serif; }

  .poster {
    position: absolute; left: 318px; top: 50px;
    width: 564px; height: 800px; overflow: hidden;
    box-shadow: 0 6px 18px rgba(0,0,0,.5);
  }
  .poster__backdrop {
    position: absolute; inset: 0;
    background:
      radial-gradient(circle at 78% 22%, rgba(255,255,255,.75) 0 60px, transparent 120px),
      radial-gradient(circle at 28% 20%, rgba(255,255,255,.55) 0 40px, transparent 110px),
      radial-gradient(circle at 50% 55%, rgba(230,245,150,.55), transparent 60%),
      linear-gradient(180deg, var(--sky) 0%, var(--aqua) 25%, #cfe88a 55%, var(--lime) 75%, var(--green) 100%);
  }

  .band { position: absolute; left: 0; width: 100%; color: var(--white); text-align: center; }
  .band--top {
    top: 0; height: 62px; padding-top: 10px;
    background: linear-gradient(180deg, var(--band-dark), var(--band-mid));
    font-family: "Cinzel", Georgia, serif; font-size: 13px; letter-spacing: 4.5px; line-height: 20px;
  }
  .band--bottom {
    bottom: 0; height: 32px; line-height: 32px;
    background: linear-gradient(180deg, var(--band-mid), var(--band-dark));
    font-family: "Cinzel", Georgia, serif; font-size: 11px; letter-spacing: .5px;
  }

  .dates {
    position: absolute; left: 40px; top: 80px;
    color: var(--ink); font-weight: 700; font-size: 38px; line-height: 42px;
  }
  .dates sup { font-size: 20px; vertical-align: 16px; line-height: 0; }

  .occasion {
    position: absolute; left: 372px; top: 96px;
    color: var(--ink); font-weight: 700; font-size: 18px; line-height: 21px;
  }

  .title {
    position: absolute; left: 0; top: 300px; width: 100%;
    text-align: center; color: var(--white);
    font-family: "Cinzel", Georgia, serif; font-weight: 400;
    font-size: 150px; line-height: 158px; letter-spacing: -4px;
    text-shadow: 0 3px 8px rgba(0,0,0,.35);
  }

  .prices {
    position: absolute; left: 40px; top: 648px;
    color: var(--ink); font-weight: 700; font-size: 14px; line-height: 18px;
  }
  .prices__amount { font-size: 18px; line-height: 22px; }
  .prices__amount span { font-size: 14px; }
  .prices__note { font-size: 10px; line-height: 12px; margin-top: 2px; }

  .venue {
    position: absolute; left: 300px; top: 644px;
    color: var(--ink); font-weight: 700; font-size: 23px; line-height: 30px;
  }
  .venue__phone { font-size: 19px; line-height: 28px; }
</style>
</head>
<body>
  <main class="poster">
    <div class="poster__backdrop" role="img" aria-label="Photograph of a dancer in silhouette mid-pose over a bright aqua and lime bokeh background"></div>

    <header class="band band--top">
      Hollis-Brandt School of Dance<br>presents
    </header>

    <p class="dates">26<sup>th</sup>-28<sup>th</sup><br>July 2012</p>
    <p class="occasion">ANNUAL<br>THEATRE<br>PERFORMANCE</p>

    <h1 class="title">HERE<br>WE GO</h1>

    <section class="prices">
      <p>Price:</p>
      <p class="prices__amount">£8 <span>adults</span></p>
      <p class="prices__amount">£7 <span>concessions</span></p>
      <p class="prices__note">tickets available<br>from the theatre box office</p>
    </section>

    <section class="venue">
      <p>LANWORTH</p>
      <p>GUILD PLAYHOUSE</p>
      <p class="venue__phone">01632 960418</p>
    </section>

    <footer class="band band--bottom">WWW.HBSCHOOLOFDANCE-EXAMPLE.CO.UK</footer>
  </main>
</body>
</html>
```